Präsentationsvorlagen/Workbook für Coaching - Yoga - Training
Zielgruppe
Coaching - Yoga - Training, d.h. Yogaunterricht, Einzelcoaching, Seminare und Workshops rund um das Thema Stress/Resilienz/Achtsamkeit
Zielgruppe sind einerseits überwiegend Frauen, aber auch Firmenkunden, die für ihre Mitarbeiter Seminare und Yoga anbieten.
Aufgabenstellung
Ich benötige einen professionellen ppt Auftritt für Präsentationen/Workbooks mit meinen Firmenfarben (grau, weiß, rosa, beige) in den mein Logo integriert ist.
Das Design sollte dem Thema entsprechend 'warm' sein aber die nötige Professionalität für Firmenkunden ausstrahlen.

```html
<!DOCTYPE html>
<html lang="de">
<head>
<meta charset="utf-8">
<title>Lena Marwitz – Präsentationsvorlage</title>
<link href="https://fonts.googleapis.com/css2?family=Cinzel:wght@400;500&family=Montserrat:wght@300;400;500&display=swap" rel="stylesheet">
<style>
  :root{
    --rose:#a5587d;
    --rose-soft:#c98aa8;
    --slate:#545a58;
    --ink:#4a4a4a;
    --muted:#9a9a9a;
    --line:#8f8f8f;
    --paper:#ffffff;
    --serif:'Cinzel', Georgia, serif;
    --sans:'Montserrat', Arial, sans-serif;
  }
  *{box-sizing:border-box;margin:0;padding:0}
  html,body{width:848px;height:1200px;overflow:hidden;background:var(--paper)}
  body{position:relative;font-family:var(--sans);color:var(--ink)}

  .slide{position:absolute;width:368px;height:207px;border:1px solid var(--line);background:var(--paper);overflow:hidden}
  .col-a{left:36px}.col-b{left:438px}
  .row-1{top:74px}.row-2{top:293px}.row-3{top:512px}.row-4{top:730px}.row-5{top:948px}

  .photo{position:absolute}
  .photo--gray{background:linear-gradient(160deg,#e6e6e6 0%,#b9b9b9 45%,#6e6e6e 100%)}
  .photo--warm{background:linear-gradient(160deg,#efe9e2 0%,#c9b6a2 45%,#3e4b6c 100%)}
  .photo--forest{background:linear-gradient(160deg,#7e8a6a 0%,#b7a98f 45%,#b69ac8 100%)}
  .photo--sea{background:linear-gradient(180deg,#5b5b5b 0%,#d8d8d8 40%,#3c3c3c 100%)}
  .photo--rose{background:linear-gradient(180deg,#e7c7d5 0%,#c07a9b 45%,#8e4d6b 100%)}
  .photo--sky{background:linear-gradient(180deg,#e9e9e9 0%,#8d8d8d 55%,#3a3a3a 100%)}

  .title{font-family:var(--serif);font-weight:400;color:var(--ink);font-size:14px;letter-spacing:.06em;position:absolute}
  .title--light{color:#fff}
  .copy{font-size:5.4px;line-height:1.75;color:var(--muted);position:absolute}
  .copy--light{color:#e9dfe4}
  .link{color:var(--rose);text-decoration:underline;text-decoration-color:var(--rose-soft)}
  .page-no{position:absolute;right:9px;bottom:6px;font-size:5px;color:var(--muted)}
  .brand-mini{position:absolute;left:10px;bottom:7px;font-family:var(--serif);font-size:4px;color:var(--muted);letter-spacing:.05em}

  .brand{position:absolute;text-align:center}
  .brand__dot{width:24px;height:24px;border-radius:50%;border:1.5px solid var(--rose);margin:0 auto 6px}
  .brand__name{font-family:var(--serif);font-size:15px;color:var(--slate);letter-spacing:.08em}
  .brand__tag{font-family:var(--serif);font-size:6px;color:var(--rose);letter-spacing:.12em;margin-top:1px}

  .agenda{position:absolute;left:30px;top:95px;list-style:none;font-size:6.5px;color:var(--muted);line-height:2}
  .agenda span{display:inline-block;width:22px}

  .offer{position:absolute;top:56px;width:71px;height:119px;background:var(--slate);padding:7px 7px}
  .offer h3{font-family:var(--serif);font-weight:400;font-size:9px;color:#fff;letter-spacing:.05em;line-height:1.05;margin-bottom:6px}
  .offer p{font-size:5px;line-height:1.6;color:var(--rose-soft)}

  .panel-rose{position:absolute;background:var(--rose)}
  .panel-slate{position:absolute;background:var(--slate)}

  .benefits{position:absolute;left:178px;top:54px;list-style:none}
  .benefits li{height:26.5px;display:flex;align-items:center;font-size:5.5px}
  .benefits b{font-family:var(--serif);font-weight:400;font-size:12px;color:var(--ink);width:16px}

  .contact{position:absolute;left:141px;width:234px;top:150px;text-align:center;font-size:4.2px;line-height:1.7;color:var(--muted)}
</style>
</head>
<body>

<!-- Titel -->
<section class="slide col-a row-1">
  <div class="photo photo--gray" style="left:0;top:0;width:155px;height:207px" role="img" aria-label="Schwarzweiß-Porträt der Coachin, sitzend am Fenster"></div>
  <div class="brand" style="left:175px;top:58px;width:180px">
    <div class="brand__dot"></div>
    <div class="brand__name">Lena Marwitz</div>
    <div class="brand__tag">Coaching · Yoga · Training</div>
  </div>
</section>

<!-- Agenda -->
<section class="slide col-b row-1">
  <h2 class="title" style="left:28px;top:56px;font-size:15px">Agenda</h2>
  <ol class="agenda">
    <li><span>1.</span>Über mich</li>
    <li><span>2.</span>Meine Angebote</li>
    <li><span>3.</span>Kontakt</li>
  </ol>
  <div class="photo photo--warm" style="left:185px;top:0;width:183px;height:207px" role="img" aria-label="Farbfoto der Coachin im blauen Kleid auf einem Korbsessel"></div>
  <div class="brand-mini">Lena Marwitz</div>
</section>

<!-- Über mich -->
<section class="slide col-a row-2">
  <div class="photo photo--forest" style="left:22px;top:22px;width:120px;height:161px" role="img" aria-label="Porträt der Coachin an einem Baum im Wald"></div>
  <h2 class="title" style="left:162px;top:44px">Über Mich</h2>
  <p class="copy" style="left:162px;top:72px;width:175px"><span class="link">Lorem ipsum dolor sit amet, consetetur sadipscing elitr, sed diam nonumy eirmod tempor invidunt ut labore et dolore magna aliquyam erat, sed diam voluptua.</span></p>
  <p class="copy" style="left:162px;top:118px;width:175px"><span class="link">Lorem ipsum dolor sit amet. Lorem ipsum dolor sit amet, consetetur sadipscing elitr, sed diam nonumy eirmod tempor invidunt ut labore et dolore.</span></p>
  <div class="brand-mini">Lena Marwitz</div>
  <span class="page-no">01</span>
</section>

<!-- Mehr über mich -->
<section class="slide col-b row-2">
  <div class="photo photo--sea" style="left:0;top:0;width:368px;height:207px" role="img" aria-label="Schwarzweißfoto einer Meeresbrandung an Felsen"></div>
  <div class="panel-rose" style="left:70px;top:42px;width:228px;height:120px"></div>
  <h2 class="title title--light" style="left:84px;top:62px">Mehr über Mich</h2>
  <p class="copy copy--light" style="left:84px;top:90px;width:200px;text-decoration:underline">Lorem ipsum dolor sit amet, consetetur sadipscing elitr, sed diam nonumy eirmod tempor invidunt ut labore et dolore magna aliquyam erat, sed diam voluptua.</p>
</section>

<!-- Meine Angebote -->
<section class="slide col-a row-3">
  <h2 class="title" style="left:24px;top:20px">Meine Angebote</h2>
  <article class="offer" style="left:35px"><h3>Coaching</h3><p class="link">Lorem ipsum dolor sit amet, consetetur sadipscing elitr, sed diam nonumy eirmod tempor invidunt ut labore et dolore magna aliquyam erat, sed diam voluptua.</p></article>
  <article class="offer" style="left:110px"><h3>Yoga</h3><p class="link">Lorem ipsum dolor sit amet, consetetur sadipscing elitr, sed diam nonumy eirmod tempor invidunt ut labore et dolore magna aliquyam erat, sed diam voluptua.</p></article>
  <article class="offer" style="left:185px"><h3>Training</h3><p class="link">Lorem ipsum dolor sit amet, consetetur sadipscing elitr, sed diam nonumy eirmod tempor invidunt ut labore et dolore magna aliquyam erat, sed diam voluptua.</p></article>
  <article class="offer" style="left:260px"><h3>Nordic Walking</h3><p class="link">Lorem ipsum dolor sit amet, consetetur sadipscing elitr, sed diam nonumy eirmod tempor invidunt ut labore et dolore magna aliquyam erat, sed diam.</p></article>
  <div class="brand-mini">Lena Marwitz</div>
  <span class="page-no">03</span>
</section>

<!-- Coaching (Foto) -->
<section class="slide col-b row-3">
  <div class="photo photo--warm" style="left:20px;top:22px;width:120px;height:161px" role="img" aria-label="Farbfoto der Coachin im Korbsessel, lächelnd"></div>
  <h2 class="title" style="left:160px;top:44px">Coaching</h2>
  <p class="copy" style="left:160px;top:70px;width:190px;color:var(--ink)">Zurück zur Selbstfürsorge und Selbstbestimmtheit</p>
  <p class="copy" style="left:160px;top:88px;width:192px;font-size:4.6px">Wo stehst Du heute? Und wo möchtest Du hin? Coaching ist ein lösungsorientierter Prozess, der Dir in herausfordernden Lebenssituationen Klarheit schenkt. Deine Situation aus verschiedenen Blickwinkeln zu betrachten, hilft Dir, neue Wege zu erkennen und Deine Ressourcen zu stärken. Mein fachliches Wissen und langjährige Erfahrung begleiten Dich achtsam, wertschätzend und vertrauensvoll auf Deinem Weg zu mehr Gelassenheit und neuer Energie.</p>
  <div class="brand-mini">Lena Marwitz</div>
  <span class="page-no">06</span>
</section>

<!-- Coaching (Landschaft) -->
<section class="slide col-a row-4">
  <div class="photo photo--rose" style="left:0;top:0;width:368px;height:207px" role="img" aria-label="Rosa getöntes Landschaftsfoto mit See, Wald und Wolken"></div>
  <div class="panel-slate" style="left:50px;top:18px;width:268px;height:182px"></div>
  <h2 class="title title--light" style="left:74px;top:36px">Coaching</h2>
  <p class="copy copy--light" style="left:74px;top:64px;width:230px">Zurück zur Selbstfürsorge und Selbstbestimmtheit</p>
  <p class="copy copy--light" style="left:74px;top:82px;width:232px;font-size:4.8px">Wo stehst Du heute? Und wo möchtest Du hin? Coaching ist ein lösungsorientierter Prozess, der Dir in herausfordernden Lebenssituationen Klarheit schenkt. Deine Situation aus verschiedenen Blickwinkeln zu betrachten, hilft Dir, neue Wege zu erkennen und Deine Ressourcen zu stärken. Mein fachliches Wissen und langjährige Erfahrung begleiten Dich achtsam, wertschätzend und vertrauensvoll auf Deinem Weg zu mehr Gelassenheit und neuer Energie.</p>
</section>

<!-- Vorteile -->
<section class="slide col-b row-4">
  <div class="panel-rose" style="left:0;top:0;width:140px;height:207px"></div>
  <h2 class="title title--light" style="left:0;width:140px;top:94px;text-align:center">Vorteile</h2>
  <ol class="benefits">
    <li><b>1</b><span class="link">Lorem ipsum dolor sit amet</span></li>
    <li><b>2</b><span class="link">Lorem ipsum dolor sit amet</span></li>
    <li><b>3</b><span class="link">Lorem ipsum dolor sit amet</span></li>
    <li><b>4</b><span class="link">Lorem ipsum dolor sit amet</span></li>
  </ol>
  <span class="page-no">06</span>
</section>

<!-- Call to Action -->
<section class="slide col-a row-5">
  <h2 class="title" style="left:8px;width:172px;top:86px;text-align:center;line-height:1.3">Worauf Wartest Du Noch?</h2>
  <div class="photo photo--sky" style="left:184px;top:0;width:184px;height:207px" role="img" aria-label="Schwarzweißfoto eines Sees unter Wolkenhimmel"></div>
  <div class="brand-mini">Lena Marwitz</div>
</section>

<!-- Danke -->
<section class="slide col-b row-5">
  <div class="photo photo--gray" style="left:22px;top:22px;width:119px;height:161px" role="img" aria-label="Schwarzweiß-Porträt der Coachin am Fenster"></div>
  <h2 class="title" style="left:141px;width:234px;top:50px;text-align:center;font-size:15px">Vielen Dank!</h2>
  <div class="brand" style="left:141px;width:234px;top:84px">
    <div class="brand__dot" style="width:20px;height:20px;margin-bottom:4px"></div>
    <div class="brand__name" style="font-size:12px">Lena Marwitz</div>
    <div class="brand__tag" style="font-size:5px">Coaching · Yoga · Training</div>
  </div>
  <address class="contact" style="font-style:normal">
    Köln, Deutschland<br>
    Lindenweg 12 · 50667 Köln<br>
    kontakt@lena-marwitz.example<br>
    +49 221 0000000
  </address>
</section>

</body>
</html>
```